Flyer for American Indian Elders on Dementia Warning Signs

We need a flyer designed for older adults who are American Indian or Alaska Native (in the U.S.).

Ideally, the flyer should complement the colors of our logos. The project logo and our organization logo are attached to the brief.

When people see the flyer we want them to feel that it represents their culture, is warm, and professional but relatable to older adults and people who have limited incomes.

I have attached an earlier draft of the document we designed ourselves BUT we want different and better.

It is for older adults who have trouble reading so:
1. you must use a font that is 11.5 points or larger
2. Do not put text over complex pictures or use shading with words
3. You can use a serif font for the heading, but should use san serif for the body text
4. There should be good contrast between the font color and background

Please do not use any images that include a head dress or pictures of American Indian people or things that are very traditional or "token" imagery.

We need to save a small space under the call out box/ somewhere on the flyer for other people to add their logo once they download.

Let us know if you have questions or need additional information.

Target Market(s)

Older American Indian people

Font styles to use
Serif
Sans Serif

Requirements
Must have
• Easy to read for older adults
Should not have
• indian headdress

```html
<!DOCTYPE html>
<html lang="en">
<head>
<meta charset="utf-8">
<title>10 Signs of Thinking or Memory Changes</title>
<link rel="stylesheet" href="https://fonts.googleapis.com/css2?family=Barlow+Condensed:wght@500;600&family=Roboto+Slab:wght@600;800&family=Montserrat:wght@500&display=swap">
<style>
  :root{
    --backdrop:#4a4a4a;
    --paper:#ffffff;
    --teal:#52a9b1;
    --blush:#f4b5ab;
    --brick:#b55a50;
    --ink:#1f1f1f;
    --tree:#f4ebe9;
  }
  *{margin:0;padding:0;box-sizing:border-box}
  html,body{width:1200px;height:1200px;overflow:hidden;background:var(--backdrop)}
  body{font-family:"Barlow Condensed",sans-serif;font-weight:500;color:var(--ink)}
  .flyer{position:absolute;left:180px;top:55px;width:842px;height:1089px;background:var(--paper);overflow:hidden}
  .header{position:absolute;left:0;top:0;width:842px;height:245px;background:var(--teal)}
  .logo-slot{position:absolute;left:0;top:0}
  .logo-placeholder{position:absolute;top:24px;font-family:"Montserrat",sans-serif;font-size:27px;color:var(--teal)}
  .title{position:absolute;left:24px;top:8px;font-family:"Roboto Slab",serif;font-weight:800;font-size:94px;letter-spacing:1px;
    background:linear-gradient(#fff 55%,#f8d2cb);-webkit-background-clip:text;background-clip:text;color:transparent;line-height:1.1}
  .subtitle{position:absolute;left:27px;top:96px;font-family:"Roboto Slab",serif;font-weight:600;font-size:22.5px;color:#fff;letter-spacing:.2px;white-space:nowrap}
  .intro{position:absolute;left:27px;width:790px;font-size:15.5px;line-height:23px;color:#fff}
  .band{position:absolute;left:0;top:245px;width:842px;height:29px}
  .tree{position:absolute;left:105px;top:274px;width:620px;height:600px}
  .sign{position:absolute;font-size:15.5px;line-height:22.5px;width:330px}
  .sign .num{position:absolute;left:-46px;top:-6px;width:34px;height:34px;border-radius:50%;background:var(--teal);color:#fff;
    font-weight:600;font-size:21px;line-height:34px;text-align:center}
  .sign h3{display:inline;font:inherit;font-weight:600;color:var(--teal)}
  .sign ul{list-style:none}
  .sign li{position:relative;padding-left:13px}
  .sign li::before{content:"";position:absolute;left:0;top:9px;width:6px;height:6px;border-radius:50%;background:var(--teal)}
  .facts{position:absolute;left:0;top:829px;width:434px;height:260px;background:var(--teal);border-top-right-radius:110px 90px}
  .facts ul{list-style:none;position:absolute;left:0;top:28px}
  .facts li{position:relative;padding-left:51px;color:#fff;font-size:14.5px;line-height:21px;margin-bottom:14px;width:420px}
  .facts svg{position:absolute;left:24px;top:3px}
  .resources{position:absolute;left:408px;top:861px;width:416px;height:158px;background:var(--brick);
    border-top-left-radius:60px 40px;border-top-right-radius:50px;border-left:0}
  .resources p{position:absolute;left:53px;top:8px;color:#fff;font-size:17px;line-height:24.5px;width:300px}
  .resources .link{position:absolute;left:53px;color:#fff;font-size:22px;display:flex;align-items:center;gap:6px}
  .partners{position:absolute;top:1030px;display:flex;align-items:center;gap:7px;font-weight:600;font-size:15px;line-height:16px}
  .partner-a{left:458px;color:var(--teal)}
  .partner-b{left:655px;color:var(--brick)}
  .partners .dot{width:34px;height:34px;border-radius:50%;background:var(--teal);flex:none}
  .partners .sq{width:26px;height:26px;background:var(--brick);flex:none}
</style>
</head>
<body>
<main class="flyer">
  <section class="header">
    <svg class="logo-slot" width="842" height="90" viewBox="0 0 842 90">
      <path d="M842 0 H508 L478 72 Q474 84 488 84 H842" fill="#fff" stroke="#f4b5ab" stroke-width="6"/>
    </svg>
    <span class="logo-placeholder" style="left:561px">Logo</span>
    <span class="logo-placeholder" style="left:663px">Logo</span>
    <h1 class="title">10 SIGNS</h1>
    <h2 class="subtitle">OF THINKING OR MEMORY CHANGES THAT MIGHT BE DEMENTIA</h2>
    <p class="intro" style="top:133px">As we get older, we may slow down a bit. This is a normal part of aging. Changes in memory or thinking that make it harder to get through the day, are not a normal part of aging. These may be early signs of dementia.</p>
    <p class="intro" style="top:186px">Because American Indian and Alaska Native people have a high risk of dementia, it is important to know the warning signs. Do you have any of these 10 signs? If so, talk to your doctor.</p>
  </section>
  <div class="band" role="img" aria-label="Decorative zigzag pattern band in white, slate and brick tones" style="background:linear-gradient(#fff 0%,#d9c5c3 40%,#a86a63 80%,#b55a50 100%)"></div>
  <div class="tree" role="img" aria-label="Faint tree with branching roots shaped like a head in profile" style="background:radial-gradient(ellipse at 50% 40%,var(--tree) 55%,rgba(244,235,233,0) 72%)"></div>

  <div class="sign" style="left:81px;top:296px"><span class="num">01</span><h3>Memory loss that affects your daily life.</h3> You may:
    <ul><li>Forget events or important dates</li><li>Repeat yourself</li><li>Rely more often on lists or sticky notes<br>to remember things</li></ul></div>
  <div class="sign" style="left:81px;top:422px;width:300px"><span class="num">02</span><h3>Trouble planning or solving problems.</h3> You may have a harder time:
    <ul><li>Paying bills</li><li>Cooking recipes you have used for years</li></ul></div>
  <div class="sign" style="left:81px;top:547px;width:340px"><span class="num">03</span><h3>Get confused about the time, date, or where you are.</h3></div>
  <div class="sign" style="left:81px;top:598px"><span class="num">04</span><h3>Daily tasks are getting harder,</h3> including:
    <ul><li>Driving</li><li>Making a grocery list or going shopping</li></ul></div>
  <div class="sign" style="left:81px;top:710px;width:310px"><span class="num">05</span><h3>Trouble with how your eyesight and thinking work together that gets worse.</h3> This includes:
    <ul><li>Tripping, falls, or problems with your balance</li><li>Spilling or dropping things more</li></ul></div>

  <div class="sign" style="left:484px;top:296px;width:345px"><span class="num">06</span><h3>New trouble talking or writing.</h3><br>You have a hard time finding the words you want to say. For example, you may say “that thing on your wrist<br>that tells time” instead of “watch.”</div>
  <div class="sign" style="left:484px;top:408px"><span class="num">07</span><h3>Lose and cannot find things.</h3> For example, you:
    <ul><li>Can’t find the coffee pot that you use every day</li><li>Might put your car keys in the freezer</li></ul></div>
  <div class="sign" style="left:484px;top:501px;width:345px"><span class="num">08</span><h3>Notice changes in mood or personality,</h3> such as being:
    <ul><li>Easily mad or sad in everyday situations</li><li>More fearful (scared) or suspicious (not trusting)</li></ul></div>
  <div class="sign" style="left:484px;top:594px;width:320px"><span class="num">09</span><h3>Act different and make poor choices.</h3> This may make you more likely to:
    <ul><li>Spend money you do not have or be a scam victim</li><li>Stop washing up regularly or pay less attention<br>to how you look</li><li>Forget to take care of your pet</li></ul></div>
  <div class="sign" style="left:484px;top:755px;width:345px"><span class="num">10</span><h3>Pull away from friends and family because it<br>is harder to keep up.</h3> You may not want to do things you used to enjoy, like sporting events, church, music, or sex.</div>

  <section class="facts">
    <ul>
      <li><svg width="18" height="18" viewBox="0 0 18 18"><circle cx="9" cy="9" r="9" fill="#fff"/><path d="M5 9.3l2.6 2.6L13 6.5" fill="none" stroke="#52a9b1" stroke-width="2.2"/></svg>American Indian and Alaska Native people have a<br>higher risk of dementia.</li>
      <li><svg width="18" height="18" viewBox="0 0 18 18"><circle cx="9" cy="9" r="9" fill="#fff"/><path d="M5 9.3l2.6 2.6L13 6.5" fill="none" stroke="#52a9b1" stroke-width="2.2"/></svg>Big changes in memory or thinking that make it hard to get through the day are not a normal part of aging.</li>
      <li><svg width="18" height="18" viewBox="0 0 18 18"><circle cx="9" cy="9" r="9" fill="#fff"/><path d="M5 9.3l2.6 2.6L13 6.5" fill="none" stroke="#52a9b1" stroke-width="2.2"/></svg>People with one or more of these 10 signs should talk to their doctor to find the cause. It is not always dementia.</li>
      <li><svg width="18" height="18" viewBox="0 0 18 18"><circle cx="9" cy="9" r="9" fill="#fff"/><path d="M5 9.3l2.6 2.6L13 6.5" fill="none" stroke="#52a9b1" stroke-width="2.2"/></svg>Early dementia diagnosis gives you a chance to<br>get care and plan your future.</li>
    </ul>
  </section>

  <section class="resources">
    <p>To learn more about the warning signs of dementia in American Indian and Alaska Native people, visit:
      <svg width="46" height="24" viewBox="0 0 46 24" style="vertical-align:middle"><path d="M2 10 Q20 -4 38 18 M32 18 L38 19 L39 12" fill="none" stroke="#fff" stroke-width="2"/></svg></p>
    <span class="link" style="top:86px"><svg width="14" height="14" viewBox="0 0 14 14"><circle cx="7" cy="7" r="6" fill="none" stroke="#fff" stroke-width="1.6"/><path d="M1 7h12M7 1q-4 6 0 12M7 1q4 6 0 12" fill="none" stroke="#fff" stroke-width="1.2"/></svg>| www.cedarridgewellness.org</span>
    <span class="link" style="top:117px"><svg width="14" height="14" viewBox="0 0 14 14"><circle cx="7" cy="7" r="6" fill="none" stroke="#fff" stroke-width="1.6"/><path d="M1 7h12M7 1q-4 6 0 12M7 1q4 6 0 12" fill="none" stroke="#fff" stroke-width="1.2"/></svg>| www.healthyagingtoday.org</span>
  </section>

  <div class="partners partner-a"><span class="dot"></span>CEDAR RIDGE<br>BRAIN WELLNESS</div>
  <div class="partners partner-b"><span class="sq"></span>CIRCLE OF ELDERS<br>NETWORK</div>
</main>
</body>
</html>
```